Stationary for Keeping Steady

we are in the process of creating a more professional image for our company Keeping Steady Paramedical Services. We have recently had a new logo and general brochure designed using artpitchhub and have been impressed by the quality of submissions.

We need:
- Letterhead (A4)
- Business Cards
- With compliments slips
- Email stationary

Letterhead information:
Address - 47 Wattlebrook Drive, Fernhollow Vic 3091
Phone - 1800 462 817
email - enquiries@keepsteady.com.au
Internet - www.keepsteady.com.au
ABN - 82 463 915 207
ACN - 264 871 035

Files need to be able to be edited in Illustrator CS2

Business Cards / with compliments slips / email stationary:
Double sided.
One side to have Name, Mobile number, company phone 1800462817, email, internet address

Files need to be able to be edited in Illustrator CS2 (except email stationary)

Our website is www.keepsteady.com.au for more information. Do not base designs on the website as it will eventually be revised.

Target Market(s)

Australian based businesses, government departments and schools. We specialise in corporate customers rather than public first aid course

Industry/Entity Type

Internet

Requirements
Must have
• Where applicable file to be editable in illustrator CS2 to allow future alterations.

```html
<!DOCTYPE html>
<html lang="en">
<head>
<meta charset="utf-8">
<title>Keeping Steady – Business Card</title>
<link href="https://fonts.googleapis.com/css2?family=Arimo:wght@400;700&display=swap" rel="stylesheet">
<style>
  :root {
    --bleed: #bcc6c6;
    --bleed-label: #ffffff;
    --card: #ffffff;
    --brand-red: #d4202e;
    --ink-dark: #1a1a1a;
    --ink-light: #ffffff;
  }
  html, body {
    margin: 0;
    padding: 0;
    width: 1200px;
    height: 720px;
    overflow: hidden;
    background: var(--bleed);
    font-family: "Arimo", Arial, sans-serif;
  }
  .canvas {
    position: relative;
    width: 1200px;
    height: 720px;
    background: var(--bleed);
  }
  .bleed-label {
    position: absolute;
    color: var(--bleed-label);
    font-size: 19px;
    letter-spacing: 0.5px;
    white-space: nowrap;
  }
  .bleed-label--top { top: 8px; }
  .bleed-label--side {
    left: 20px;
    transform: translate(-50%, -50%) rotate(-90deg);
  }
  .card {
    position: absolute;
    left: 40px;
    top: 40px;
    width: 1123px;
    height: 640px;
    background: var(--card);
    overflow: hidden;
  }
  .card__panel {
    position: absolute;
    inset: 0;
    width: 1123px;
    height: 640px;
  }
  .brand {
    position: absolute;
    left: 42px;
    top: 250px;
    display: flex;
    align-items: center;
    gap: 22px;
  }
  .brand__mark {
    width: 34px;
    height: 34px;
    background: var(--brand-red);
  }
  .brand__name {
    color: var(--brand-red);
    font-weight: 700;
    font-size: 58px;
    letter-spacing: -0.5px;
  }
  .registration {
    position: absolute;
    left: 42px;
    top: 545px;
    color: var(--ink-dark);
    font-weight: 700;
    font-size: 20px;
    line-height: 31px;
    letter-spacing: 0.5px;
  }
  .contact {
    position: absolute;
    right: 44px;
    color: var(--ink-light);
    text-align: right;
    white-space: nowrap;
  }
  .contact__name {
    top: 95px;
    font-size: 42px;
  }
  .contact__role {
    top: 145px;
    font-size: 33px;
  }
  .contact__address {
    top: 335px;
    font-size: 31px;
    line-height: 42px;
  }
  .contact__lines {
    top: 452px;
    font-size: 30px;
    line-height: 37px;
  }
</style>
</head>
<body>
<div class="canvas">
  <span class="bleed-label bleed-label--top" style="left:306px">edge out area</span>
  <span class="bleed-label bleed-label--top" style="left:520px">edge out area</span>
  <span class="bleed-label bleed-label--top" style="left:733px">edge out area</span>
  <span class="bleed-label bleed-label--side" style="top:125px">edge out area</span>
  <span class="bleed-label bleed-label--side" style="top:345px">edge out area</span>
  <span class="bleed-label bleed-label--side" style="top:560px">edge out area</span>

  <div class="card">
    <svg class="card__panel" viewBox="0 0 1123 640" aria-hidden="true">
      <defs>
        <radialGradient id="panelGlow" cx="600" cy="170" r="620" gradientUnits="userSpaceOnUse">
          <stop offset="0" stop-color="#c8141e"/>
          <stop offset="0.25" stop-color="#7a0b12"/>
          <stop offset="0.6" stop-color="#1e1212"/>
          <stop offset="1" stop-color="#101010"/>
        </radialGradient>
      </defs>
      <path d="M674,0 C600,150 575,470 470,640 L1123,640 L1123,0 Z" fill="url(#panelGlow)"/>
    </svg>

    <div class="brand">
      <span class="brand__mark"></span>
      <span class="brand__name">Keeping Steady</span>
    </div>

    <div class="registration">
      <div>ABN - 82 463 915 207</div>
      <div>ACN - 264 871 035</div>
    </div>

    <div class="contact contact__name">Marla ‘Mel’ Quinn</div>
    <div class="contact contact__role">Northgate Ward Character</div>
    <div class="contact contact__address">
      <div>47 Wattlebrook Drive,</div>
      <div>Fernhollow Vic 3091</div>
    </div>
    <div class="contact contact__lines">
      <div>M: 912 345 6780</div>
      <div>P: 1800 462 817</div>
      <div>E: enquiries@keepsteady.com.au</div>
      <div>W: www.keepsteady.com.au</div>
    </div>
  </div>
</div>
</body>
</html>
```